Funeral Services Site

We need a website for a Funeral Services company. The old website is: www.rouwcentrumkorvelaer.be We need the same structure and text.

Target Market(s)

Customers.

Coding

Coded - Design and coding required

Number of Pages Required

4 page

Font styles to use
Serif
Sans Serif
Script

```html
<!DOCTYPE html>
<html lang="en">
<head>
<meta charset="utf-8">
<title>Funeral Home Korvelaer</title>
<link rel="stylesheet" href="https://fonts.googleapis.com/css2?family=Poppins:wght@300;400;500;600;700;800&display=swap">
<style>
:root{
  --ink:#4b4b4b;
  --ink-soft:#5e5e5e;
  --dark:#565656;
  --footer:#575757;
  --white:#ffffff;
  --line:#d8d8d8;
}
*{box-sizing:border-box;margin:0;padding:0}
html,body{width:1200px;height:3742px;overflow:hidden}
body{position:relative;background:var(--white);font-family:'Poppins',sans-serif;color:var(--ink)}
.abs{position:absolute}
a{color:inherit;text-decoration:none}

/* hero */
.hero-photo{left:0;top:0;width:1110px;height:722px}
.brand{left:90px;top:18px;display:flex;align-items:center;gap:14px;color:var(--white)}
.brand-dot{width:70px;height:70px;border:2px solid var(--white);border-radius:50%}
.brand-name{font-weight:600;font-size:22px;line-height:24px}
.nav{top:30px;left:0;width:1110px;height:20px;font-size:12.5px;font-weight:500;color:var(--white);letter-spacing:.2px}
.nav span{position:absolute;top:0;white-space:nowrap}
.flag{left:1013px;top:-5px;width:30px;height:30px;border-radius:50%;background:linear-gradient(#b22234 0 14%,#fff 14% 28%,#b22234 28% 42%,#fff 42% 56%,#b22234 56% 70%,#fff 70% 84%,#b22234 84%);overflow:hidden}
.flag::after{content:"";position:absolute;left:0;top:0;width:14px;height:14px;background:#3c3b6e}
.scroll{left:1150px;top:222px;writing-mode:vertical-rl;transform:rotate(180deg);font-size:11px;color:#777}
.scroll-line{left:1159px;top:265px;width:1px;height:20px;background:#555}
.hero-kicker{left:86px;top:252px;font-size:34px;font-weight:700;color:var(--white);letter-spacing:.5px}
.hero-kicker::after{content:"";position:absolute;left:0;bottom:2px;width:100%;height:3px;background:rgba(255,255,255,.5)}
.hero-title{left:84px;top:286px;font-size:84px;line-height:100px;font-weight:800;color:var(--white);letter-spacing:1px}
.hero-title::after{content:"";position:absolute;left:0;bottom:10px;width:100%;height:4px;background:rgba(255,255,255,.5)}
.hero-legal{left:598px;top:302px;font-size:19px;color:var(--white)}
.hero-sub{left:86px;top:400px;font-size:19px;color:var(--white);font-weight:300}
.btn{display:flex;align-items:center;justify-content:center;font-size:13px;font-weight:500;letter-spacing:.3px}
.btn-light{background:var(--white);color:#222}
.btn-ghost-light{border:2px solid var(--white);color:var(--white)}
.btn-outline{border:2px solid #555;color:#444;border-radius:3px}
.btn-dark{background:var(--dark);color:var(--white)}

/* sections */
.photo{border:0}
.h2{font-size:43px;font-weight:700;color:var(--ink);letter-spacing:.5px}
.lead{font-size:24px;font-weight:300;color:var(--ink);line-height:28px}
.body{font-size:12.5px;line-height:19.5px;color:var(--ink-soft);text-align:justify}
.checks{list-style:none;font-size:13px;color:var(--ink-soft)}
.checks li{position:relative;padding-left:24px;margin-bottom:19px;line-height:19px}
.checks svg{position:absolute;left:0;top:3px}
.card{border-radius:0 0 0 30px}

.q-kicker{left:580px;top:2640px;font-size:31px;font-weight:600;color:var(--ink);letter-spacing:.5px}
.q-kicker::after{content:"";position:absolute;left:0;bottom:0;width:100%;height:3px;background:#cfcfcf}
.q-title{left:578px;top:2672px;font-size:88px;line-height:104px;font-weight:800;color:var(--ink);letter-spacing:2px}
.q-title::after{content:"";position:absolute;left:0;bottom:4px;width:100%;height:3px;background:#cfcfcf}
.q-text{left:582px;top:2788px;font-size:20px;line-height:31px;font-weight:300;color:var(--ink)}

/* footer */
.footer{left:0;top:3330px;width:1200px;height:412px;background:var(--footer);color:var(--white)}
.footer-band{left:0;top:3150px;width:1200px;height:182px;background:linear-gradient(to bottom,rgba(87,87,87,0) 0%,rgba(87,87,87,.55) 45%,var(--footer) 100%)}
.f-brand{left:102px;top:3410px;display:flex;align-items:center;gap:12px;color:var(--white);font-size:26px;font-weight:600}
.f-brand i{display:block;width:54px;height:54px;border:2px solid var(--white);border-radius:50%}
.social{top:3561px;width:36px;height:36px;border-radius:50%;background:#666;border:1px solid #777}
.f-head{font-size:19px;font-weight:600;color:var(--white)}
.f-links{list-style:none;font-size:12px;color:#f0f0f0}
.f-links li{height:31px;padding-left:10px;position:relative}
.f-links li::before{content:"›";position:absolute;left:0;top:-1px;color:#aaa}
.f-info{font-size:12px;line-height:16px;color:#f0f0f0}
.f-info b{font-weight:600;display:block}
.f-info div{position:relative;padding-left:19px;margin-bottom:16px}
.f-info svg{position:absolute;left:0;top:2px}
.news-input{left:867px;top:3450px;width:241px;height:34px;background:#6a6a6a;font-size:12px;color:#e6e6e6;display:flex;align-items:center;padding-left:18px;gap:8px}
.news-send{left:867px;top:3496px;width:90px;height:43px;background:var(--white);color:#333;font-size:13px;font-weight:500}
.copy{left:0;top:3703px;width:1200px;text-align:center;font-size:12px;color:#eee}
.to-top{left:1138px;top:3666px;width:34px;height:34px;border-radius:50%;background:var(--white);display:flex;align-items:center;justify-content:center}
</style>
</head>
<body>

<!-- hero -->
<svg class="abs hero-photo" viewBox="0 0 1110 722" role="img" aria-label="White roses bouquet lying on a wooden deck">
  <defs>
    <linearGradient id="heroTone" x1="0" y1="0" x2="1" y2="0.6">
      <stop offset="0" stop-color="#7d7872"/>
      <stop offset="0.45" stop-color="#9a958d"/>
      <stop offset="0.7" stop-color="#c9c8b6"/>
      <stop offset="1" stop-color="#e7e6d6"/>
    </linearGradient>
  </defs>
  <path d="M0 0H1110V420Q1110 495 1030 515L0 722Z" fill="url(#heroTone)"/>
</svg>

<div class="abs brand"><span class="brand-dot"></span><span class="brand-name">Korvelaer</span></div>
<nav class="abs nav">
  <span style="left:481px">HOME</span>
  <span style="left:555px">ABOUT US</span>
  <span style="left:654px">CONDOLE ONLINE</span>
  <span style="left:796px">ORDER FLOWERS</span>
  <span style="left:934px">CONTACT</span>
  <span style="left:1050px">ENG ⌄</span>
</nav>
<div class="abs flag" aria-hidden="true"></div>
<div class="abs scroll">Scroll</div>
<div class="abs scroll-line"></div>

<div class="abs hero-kicker">FUNERAL HOME</div>
<h1 class="abs hero-title">KORVELAER</h1>
<div class="abs hero-legal">bvba:</div>
<p class="abs hero-sub">A personal service in farewell guidance</p>
<a class="abs btn btn-light" style="left:87px;top:453px;width:125px;height:42px">012 34 56 78</a>
<a class="abs btn btn-ghost-light" style="left:227px;top:453px;width:125px;height:42px">CONTACT US</a>

<!-- about -->
<div class="abs photo" role="img" aria-label="Basket arrangement of white carnations and lilies" style="left:87px;top:705px;width:400px;height:530px;background:radial-gradient(ellipse 48% 46% at 50% 42%,#dfe6d6 0%,#b8c8a6 45%,rgba(255,255,255,0) 75%)"></div>
<h2 class="abs h2" style="left:559px;top:786px">About Us</h2>
<p class="abs lead" style="left:559px;top:845px;width:540px">Mourning center Korvelaer, a complete service in mourning and farewell guidance</p>
<p class="abs body" style="left:559px;top:928px;width:528px">Saying goodbye to a loved one is one of the toughest things in a lifetime. Funeral home Korvelaer in Hoveldorp takes care of all the practical and administrative matters involved. So you can say goodbye in peace.</p>
<p class="abs body" style="left:559px;top:1011px;width:528px">Our people have a r uime experience in farewell guidance and stand for 24 hours at 24 hours for you. Our fully renovated funeral home is open to you and your acquaint-ances, so that you can greet your loved one at any time of the day.</p>
<a class="abs btn btn-outline" style="left:562px;top:1090px;width:124px;height:50px;font-size:11px">FIND OUT MORE</a>

<!-- organization -->
<svg class="abs" style="left:623px;top:1274px" width="577" height="735" viewBox="0 0 577 735" role="img" aria-label="Pink lisianthus and white daisies on a wooden door">
  <defs>
    <radialGradient id="orgTone" cx="0.45" cy="0.42" r="0.7">
      <stop offset="0" stop-color="#d9c3c6"/>
      <stop offset="0.35" stop-color="#8a5d3f"/>
      <stop offset="0.8" stop-color="#5b3a24"/>
      <stop offset="1" stop-color="#bdb3a6"/>
    </radialGradient>
  </defs>
  <path d="M0 0H577V735L160 605Q0 555 0 440Z" fill="url(#orgTone)"/>
</svg>
<h2 class="abs h2" style="left:89px;top:1348px">Our Organization</h2>
<p class="abs lead" style="left:89px;top:1403px">Funeral and worship</p>
<p class="abs body" style="left:89px;top:1456px;width:477px">The organization of the funeral ceremony is a moment of reflection, where the personality of the deceased can be beautifully highlighted. Our team will assist you in this and select the most beautiful texts, songs and photos with you in order to arrive at an appropriate and worthy goodbye.</p>
<p class="abs body" style="left:89px;top:1549px;width:455px">The funeral can take place in your parish church or our auditorium if you wish, which can accommodate a maximum of 100 guests. We can arrange the following for you:</p>
<ul class="abs checks" style="left:89px;top:1642px;width:480px">
  <li><svg width="15" height="15" viewBox="0 0 16 16"><circle cx="8" cy="8" r="8" fill="#5a5a5a"/><path d="M4.5 8.2l2.3 2.3 4.6-4.8" stroke="#fff" stroke-width="1.8" fill="none"/></svg>Vigil the night before the funeral</li>
  <li><svg width="15" height="15" viewBox="0 0 16 16"><circle cx="8" cy="8" r="8" fill="#5a5a5a"/><path d="M4.5 8.2l2.3 2.3 4.6-4.8" stroke="#fff" stroke-width="1.8" fill="none"/></svg>Prayer service with priest (if possible)</li>
  <li><svg width="15" height="15" viewBox="0 0 16 16"><circle cx="8" cy="8" r="8" fill="#5a5a5a"/><path d="M4.5 8.2l2.3 2.3 4.6-4.8" stroke="#fff" stroke-width="1.8" fill="none"/></svg>Eucharistic celebration with priest<br>(on Tuesday and Friday in the parishes of Hoveldorp)</li>
</ul>

<!-- order flowers -->
<h2 class="abs h2" style="left:87px;top:1881px">Orders Flowers</h2>
<div class="abs card" role="img" aria-label="Single rose laid on a grey concrete block" style="left:89px;top:1971px;width:318px;height:346px;background:linear-gradient(160deg,#7d8079 0%,#a9aba4 50%,#8f918b 100%)"></div>
<div class="abs card" role="img" aria-label="Peach rose bouquet beside a perfume bottle" style="left:443px;top:2060px;width:317px;height:346px;background:linear-gradient(160deg,#c9cdc6 0%,#e6d6c8 50%,#bfc4bd 100%)"></div>
<div class="abs card" role="img" aria-label="Lily of the valley sprigs on lined kraft paper" style="left:793px;top:2150px;width:317px;height:346px;background:linear-gradient(160deg,#c7ad88 0%,#d9c3a3 55%,#c2a67f 100%)"></div>

<!-- questions -->
<div class="abs" role="img" aria-label="White carnations with dark stems on a light background" style="left:0;top:2499px;width:610px;height:654px;background:radial-gradient(ellipse 55% 55% at 32% 50%,#6e725f 0%,#b9b8a9 45%,#f3efe9 72%,rgba(255,255,255,0) 100%)"></div>
<div class="abs q-kicker">DO YOU HAVE ANY</div>
<h2 class="abs q-title">QUESTIONS</h2>
<p class="abs q-text">Or whould you like to call in our funeral home?<br>contact us. we are here for you</p>
<a class="abs btn btn-dark" style="left:583px;top:2874px;width:125px;height:43px">012 34 56 78</a>
<a class="abs btn btn-outline" style="left:722px;top:2874px;width:125px;height:43px;border-radius:0">CONTACT US</a>

<!-- footer -->
<div class="abs footer-band" role="img" aria-label="Silhouette of hills, reeds and flowers"></div>
<footer class="abs footer"></footer>
<div class="abs f-brand"><i></i>Korvelaer</div>
<span class="abs social" style="left:91px" aria-label="Social profile"></span>
<span class="abs social" style="left:142px" aria-label="Social profile"></span>
<span class="abs social" style="left:191px" aria-label="Social profile"></span>
<span class="abs social" style="left:242px" aria-label="Social profile"></span>

<div class="abs f-head" style="left:359px;top:3400px">Quick Links</div>
<ul class="abs f-links" style="left:359px;top:3446px">
  <li>Home</li><li>About Us</li><li>Condole Online</li><li>Order Flowers</li><li>Contact Us</li>
</ul>

<div class="abs f-head" style="left:555px;top:3400px">Information</div>
<div class="abs f-info" style="left:555px;top:3446px;width:290px">
  <div><svg width="12" height="10" viewBox="0 0 12 10"><rect width="12" height="10" rx="1" fill="#fff"/><path d="M0.5 1l5.5 4.2 5.5-4.2" stroke="#575757" stroke-width="1.3" fill="none"/></svg><b>Emial</b>info@rouwcentrumkorvelaer.be</div>
  <div><svg width="12" height="12" viewBox="0 0 24 24"><path d="M6.6 10.8a15 15 0 0 0 6.6 6.6l2.2-2.2a1 1 0 0 1 1-.25 11.4 11.4 0 0 0 3.6.57 1 1 0 0 1 1 1V20a1 1 0 0 1-1 1A17 17 0 0 1 3 4a1 1 0 0 1 1-1h3.5a1 1 0 0 1 1 1 11.4 11.4 0 0 0 .57 3.6 1 1 0 0 1-.25 1z" fill="#fff"/></svg><b>24/24, 7 out of 7</b>Call Us: 012 34 56 78</div>
  <div><svg width="10" height="13" viewBox="0 0 10 14"><path d="M5 0a5 5 0 0 0-5 5c0 3.8 5 9 5 9s5-5.2 5-9a5 5 0 0 0-5-5zm0 7a2 2 0 1 1 0-4 2 2 0 0 1 0 4z" fill="#fff"/></svg><b>Address</b>Lindeweg 14, 3700 Hoveldorp</div>
</div>

<div class="abs f-head" style="left:866px;top:3400px">Newsletter</div>
<div class="abs news-input"><svg width="12" height="10" viewBox="0 0 12 10"><rect width="12" height="10" rx="1" fill="#bbb"/><path d="M0.5 1l5.5 4.2 5.5-4.2" stroke="#6a6a6a" stroke-width="1.3" fill="none"/></svg>Enter your email address</div>
<a class="abs btn news-send">SEND</a>

<div class="abs copy">© Copyright 2019 &nbsp;All Rights Reserved</div>
<a class="abs to-top" aria-label="Back to top"><svg width="12" height="12" viewBox="0 0 12 12"><path d="M6 11V1M2 5l4-4 4 4" stroke="#555" stroke-width="1.4" fill="none"/></svg></a>

</body>
</html>
```